Business card design needed

I am branching out into the world of private practice in Speech Pathology. My clients will be aged 0-17; the business card will be distributed within my existing teacher and parent networks in schools.

I work with clients to develop their speech, language, literacy, fluency, swallowing and voice. I like to think that parents hand over their money to me because I've offered a fun session with positive outcomes/growth and for an affordable price.

I'm flexible with colours; though think something bright would be ideal. I'm not wanting anything too cutesy or 'little kid'. I'd like for it to stand out in a bulging purse or on a fridge crammed with papers.

Industry/Entity Type

Teacher

Contact Information for Business Card

Wren Hollow Speech Pathology Pty Ltd
Molly Fenwick
Speech Pathologist
Ph: 0419 826 307
Email: mollyfenwick@quillpost.com

Logo Text

Logo styles of interest
Character Logo
Wordmark Logo
Lettermark Logo
Requirements
Must have
• A kind of graphic to represent the core business - that is, providing intervention to children 0-17 with communication needs (e.g., speech, language, literacy, swallowing, voice, fluency)

Should not have
• Pictures of babies or children.
Love hearts.

```html
<!DOCTYPE html>
<html lang="en">
<head>
<meta charset="utf-8">
<title>Wren Hollow Speech Pathology – Business Card</title>
<link rel="stylesheet" href="https://fonts.googleapis.com/css2?family=Open+Sans:wght@400;600;700&family=Cinzel:wght@400&display=swap">
<style>
  :root {
    --page-bg: #eeebe6;
    --card-core: #f2951f;
    --card-mid: #d8661f;
    --card-edge: #922326;
    --ink: #ffffff;
    --rule: rgba(255, 240, 220, 0.85);
    --shadow: rgba(60, 30, 10, 0.45);
  }
  * { box-sizing: border-box; margin: 0; padding: 0; }
  html, body {
    width: 1200px;
    height: 1000px;
    overflow: hidden;
    background: var(--page-bg);
  }
  .sheet {
    position: relative;
    width: 1200px;
    height: 1000px;
  }
  .card {
    position: absolute;
    top: 349px;
    width: 536px;
    height: 302px;
    border-radius: 9px;
    background: radial-gradient(ellipse 62% 70% at 50% 50%, var(--card-core) 0%, var(--card-mid) 48%, var(--card-edge) 100%);
    box-shadow: 3px 5px 7px var(--shadow);
    color: var(--ink);
    font-family: "Open Sans", Arial, sans-serif;
    overflow: hidden;
  }
  .card--front { left: 47px; }
  .card--back { left: 618px; }

  .holder {
    position: absolute;
    right: 23px;
    top: 22px;
    text-align: right;
  }
  .holder__name {
    font-size: 23px;
    font-weight: 600;
    line-height: 1.1;
  }
  .holder__role {
    margin-top: 6px;
    font-size: 14px;
    font-weight: 700;
  }
  .company {
    position: absolute;
    left: 0;
    right: 0;
    top: 137px;
    text-align: center;
    font-family: "Cinzel", "Times New Roman", serif;
    font-size: 18px;
    letter-spacing: 0.6px;
  }
  .contact {
    position: absolute;
    left: 21px;
    top: 230px;
    list-style: none;
  }
  .contact__item {
    display: flex;
    align-items: center;
    height: 24px;
    font-size: 15px;
  }
  .contact__icon {
    width: 20px;
    height: 20px;
    margin-right: 10px;
    flex: none;
  }

  .rule {
    position: absolute;
    left: 50px;
    right: 50px;
    height: 2px;
    background: linear-gradient(90deg, transparent, var(--rule) 20%, var(--rule) 80%, transparent);
  }
  .rule--top { top: 70px; }
  .rule--bottom { top: 230px; }
  .mission {
    position: absolute;
    left: 167px;
    top: 98px;
    width: 200px;
    font-size: 15px;
    line-height: 21px;
    text-align: justify;
    text-align-last: left;
  }
</style>
</head>
<body>
<main class="sheet">
  <section class="card card--front" aria-label="Business card front">
    <header class="holder">
      <p class="holder__name">Molly Fenwick</p>
      <p class="holder__role">Speech Pathologist</p>
    </header>
    <p class="company">Wren Hollow Speech Pathology Pty Ltd</p>
    <ul class="contact">
      <li class="contact__item">
        <svg class="contact__icon" viewBox="0 0 20 20" aria-hidden="true">
          <circle cx="10" cy="10" r="9" fill="none" stroke="#fff" stroke-width="1.4"/>
          <path d="M6.3 5.6c.5-.5 1.2-.5 1.6 0l1 1.2c.4.5.3 1.1-.1 1.5l-.6.5c.5 1.1 1.4 2 2.5 2.6l.5-.6c.4-.4 1-.5 1.5-.1l1.2 1c.5.4.5 1.1 0 1.6l-.7.7c-.6.6-1.6.7-2.4.3-2.2-1.1-3.9-2.8-5-5-.4-.8-.3-1.8.3-2.4z" fill="#fff"/>
        </svg>
        <span>0419 826 307</span>
      </li>
      <li class="contact__item">
        <svg class="contact__icon" viewBox="0 0 20 20" aria-hidden="true">
          <circle cx="10" cy="10" r="9" fill="none" stroke="#fff" stroke-width="1.4"/>
          <text x="10" y="14" text-anchor="middle" font-family="Open Sans, Arial, sans-serif" font-size="12" font-weight="700" fill="#fff">@</text>
        </svg>
        <span>mollyfenwick@quillpost.com</span>
      </li>
    </ul>
  </section>

  <section class="card card--back" aria-label="Business card back">
    <div class="rule rule--top"></div>
    <p class="mission">Providing fun, effective and affordable intervention to support development of speech and language skills in children and adolescents</p>
    <div class="rule rule--bottom"></div>
  </section>
</main>
</body>
</html>
```